Holvery Real Estate Management Consulting

To design a high end company profile that inspires confidence in high net worth individuals and similar clients. The profile to include real estate images, preferably real images. The firm is a Zambian firm and has its target to be comparable to Tesk & Company, Parlowe & Company, Wilder Osten, Lun dorv pelsin wilder osten, TLAV Real estate company as such.

Target Market(s)

Real estate clients such as high net worth individuals, private and public companies, government and international agencies, banks and insurance companies, trusts and pension funds and individual investors. the sub target market group being developers, planners, financiers, market analysts, designers, economists, engineers, architects, construction managers, quantity surveyors and public officials and others

Colors

Designer to choose colors to be used in the design.

Requirements
Must have
• Company logo

```html
<!DOCTYPE html>
<html lang="en">
<head>
<meta charset="utf-8">
<title>Holvery Real Estate – Company Profile Spreads</title>
<link href="https://fonts.googleapis.com/css2?family=Michroma&family=Raleway:wght@300;400;600;700&display=swap" rel="stylesheet">
<style>
:root{
  --stage:#5a5a5a;
  --paper:#ffffff;
  --navy:#1f3a93;
  --navy-soft:#3552b0;
  --ink:#333333;
  --muted:#777777;
  --dark:#2b2b2b;
}
*{box-sizing:border-box;margin:0;padding:0}
html,body{width:906px;height:1200px;overflow:hidden;background:var(--stage)}
body{position:relative;font-family:"Raleway",sans-serif;color:var(--ink)}
.page{position:absolute;width:342px;height:484px;background:var(--paper);overflow:hidden}
.cover{left:84px;top:42px}
.inside-left{left:484px;top:42px}
.inside-right{left:84px;top:608px}
.back{left:482px;top:608px}
.caption{position:absolute;width:342px;text-align:center;color:#fff;font-size:21px;font-weight:400;letter-spacing:.5px}
.abs{position:absolute}
.brand{text-align:center;font-family:"Michroma",sans-serif;color:var(--navy);font-size:10px;letter-spacing:.3px}
.brand-sub{text-align:center;font-size:5.4px;color:var(--muted);letter-spacing:.4px;margin-top:2px}
.photo{position:absolute}
.tiny{font-size:4.3px;line-height:1.45;color:#666}
.h{font-size:8.5px;color:#444;font-weight:400;margin-bottom:3px}
.h b{color:var(--navy);font-weight:700}
/* page 1 */
.split-dark{position:absolute;left:170px;top:0;width:172px;height:484px;background:linear-gradient(180deg,#2a2a2a,#3c3c3c)}
.motto{position:absolute;top:12px;font-family:"Raleway",sans-serif;font-weight:700;font-size:25px;letter-spacing:8px}
.bullet-circle{position:absolute;width:28px;height:28px;border-radius:50%;background:#fff;left:156px}
.bullet-circle span{position:absolute;left:9px;top:9px;width:10px;height:10px;border-radius:50%;background:var(--dark)}
.svc{position:absolute;left:206px;width:126px;color:#ddd}
.svc .h{color:#fff}
.svc .scope{font-size:4.5px;color:#aaa;margin-bottom:2px;letter-spacing:.3px}
.svc .tiny{color:#ccc}
/* page 2 */
.band{position:absolute;left:0;top:0;width:342px;height:42px;background:var(--navy)}
.band-title{position:absolute;left:20px;top:6px;font-family:"Raleway",sans-serif;font-weight:700;font-size:30px;letter-spacing:10px;color:var(--navy-soft)}
.ticks{display:grid;grid-template-columns:1fr 1fr;column-gap:10px}
.ticks li{list-style:none;font-size:4.3px;color:#555;line-height:1.9}
.ticks li::before{content:"✓";display:inline-block;width:5px;height:5px;border:.5px solid #555;border-radius:50%;font-size:3.4px;line-height:5px;text-align:center;margin-right:3px}
.ticks li.lead::before{content:none}
.ticks li.lead{padding-left:8px}
</style>
</head>
<body>

<!-- COVER -->
<section class="page cover">
  <div class="abs" style="left:0;top:36px;width:342px">
    <div class="brand">HOLVERY REAL ESTATE</div>
    <div class="brand-sub">REGISTERED PROPERTY VALUATION SURVEYORS</div>
  </div>
  <svg class="abs" style="left:0;top:94px" width="342" height="280" viewBox="0 0 342 280">
    <polygon points="120,28 342,0 342,24 120,28" fill="#cfcfcf"/>
    <polygon points="200,22 342,4 342,28 230,28" fill="#a9a9a9"/>
  </svg>
  <div class="photo" role="img" aria-label="Grey sky above city towers" style="left:0;top:130px;width:94px;height:68px;background:linear-gradient(160deg,#e0e0e0,#8d8d8d)"></div>
  <div class="photo" role="img" aria-label="Blue glass skyscraper seen from below against a bright sky" style="left:96px;top:122px;width:162px;height:220px;background:linear-gradient(170deg,#eef2f6 0%,#9fb4cc 35%,#3a5f93 70%,#1e3150 100%)"></div>
  <div class="photo" role="img" aria-label="Office tower facade in grey tones" style="left:260px;top:122px;width:82px;height:134px;background:linear-gradient(200deg,#d7d7d7,#6e6e6e)"></div>
  <div class="photo" role="img" aria-label="Blue glass facade detail" style="left:0;top:200px;width:92px;height:74px;background:linear-gradient(160deg,#a9bcd2,#34507a)"></div>
  <div class="photo" role="img" aria-label="Dark building corner" style="left:0;top:277px;width:60px;height:65px;background:linear-gradient(160deg,#8a8a8a,#2c2c2c)"></div>
  <div class="photo" role="img" aria-label="Building section in grey" style="left:62px;top:277px;width:32px;height:65px;background:linear-gradient(160deg,#bdbdbd,#555)"></div>
  <div class="photo" role="img" aria-label="Steel and glass facade grid" style="left:260px;top:258px;width:82px;height:84px;background:linear-gradient(160deg,#cfcfcf,#3b3b3b)"></div>
  <svg class="abs" style="left:0;top:342px" width="342" height="30" viewBox="0 0 342 30">
    <polygon points="0,0 204,0 182,28 0,28" fill="var(--navy)"/>
  </svg>
  <div class="abs" style="left:0;top:384px;width:342px;text-align:center;font-family:'Michroma',sans-serif;font-size:20px;line-height:27px;color:#7a7a7a">HOLVERY REAL<br>ESTATE</div>
  <div class="abs" style="left:0;top:439px;width:342px;text-align:center;font-size:8.4px;color:#333">ACCELERATE SUCCESS....</div>
  <div class="abs" style="left:0;top:463px;width:342px;text-align:center;font-size:5.5px;letter-spacing:2.4px;color:#444">WWW.YOURWEBSITE.COM</div>
</section>
<div class="caption" style="left:84px;top:543px">COVER</div>

<!-- PAGE 1 -->
<section class="page inside-left">
  <div class="photo" role="img" aria-label="Hazy city skyline in grey" style="left:0;top:300px;width:170px;height:184px;background:linear-gradient(180deg,#fff 0%,#dcdcdc 45%,#b5b5b5 100%)"></div>
  <div class="split-dark"></div>
  <div class="photo" role="img" aria-label="Dark city skyline at dusk" style="left:170px;top:340px;width:172px;height:144px;background:linear-gradient(180deg,rgba(60,60,60,0),#1c1c1c)"></div>
  <div class="motto" style="left:25px;color:#e2e2e2">INSPIRE <span style="color:#6a6a6a">VALUE</span></div>

  <div class="abs" style="left:20px;top:82px;width:140px">
    <div class="h">WHO <b>WE ARE</b></div>
    <p class="tiny">Holvery Management Consulting is one of Zambia's leading professional real estate services firms with an outstanding reputation and has its cornerstone the excellence of its people. Since its inception, the business has continued successfully with a national client base, a number of which have retained our services.</p>
  </div>
  <div class="abs" style="left:20px;top:175px;width:140px">
    <div class="h">OUR <b>SOLUTIONS</b></div>
    <p class="tiny">As a preferred property firm we continually monitor property value levels and will provide you with an update on market rents, trends and the position of your property in the marketplace.</p>
    <p class="tiny" style="margin-top:5px">We continue to roll out our real estate services for you our clients to benefit from the power of our massive experience and database.</p>
    <p class="tiny" style="margin-top:5px">Our system allows you to save on unnecessary research costs and time of doing new research in the marketplace and all due diligence is done when identifying the interests, benefits and rights being researched.</p>
    <p class="tiny" style="margin-top:5px">We assure our clients and prospective clients that our work is independent, objective and compliant with nationally recognized Laws of the Republic of Zambia.</p>
  </div>
  <div class="abs" style="left:8px;top:452px;width:80px;font-family:'Michroma',sans-serif;font-size:5px;color:var(--navy)">HOLVERY REAL ESTATE</div>

  <div class="bullet-circle" style="top:98px"><span></span></div>
  <div class="bullet-circle" style="top:226px"><span></span></div>
  <div class="bullet-circle" style="top:344px"><span></span></div>

  <div class="svc" style="top:94px">
    <div class="h">CORE <b style="color:#fff">SERVICES</b></div>
    <div class="scope">SCOPE</div>
    <p class="tiny">Advisory Services<br>Acquisition, Leasing &amp; Disposal Advise<br>Business Plans<br>Feasibility studies<br>Highest and Best Use Studies<br>Market research/analysis<br>Planning and development<br>Property Condition Assessments</p>
  </div>
  <div class="svc" style="top:210px">
    <div class="h"><b style="color:#fff">Valuations</b></div>
    <div class="scope">SCOPE</div>
    <p class="tiny">Agriculture Valuations<br>Asset Valuations<br>Commercial Valuations<br>Leisure/Hotels/Lodges<br>Industrial Valuations<br>Special purpose Valuations<br>Mines Valuations<br>Residential Valuations<br>Plant, Machinery &amp; Equipment</p>
  </div>
  <div class="svc" style="top:330px">
    <div class="h">Firm's <b style="color:#fff">Reference</b></div>
    <div class="scope">SCOPE</div>
    <p class="tiny">The Surveyors Listing Council<br>P.O Box 50911<br>Lusaka</p>
  </div>
  <div class="svc" style="top:380px;left:204px;width:132px">
    <div class="h">Our address <b style="color:#fff">is as follows:</b></div>
    <p class="tiny">Messrs. Holvery Management Consulting<br>Unit 7, Plot No. 2218<br>Meridian Road<br>Kafue, Lusaka Province – Zambia<br>Mobile: +260 900 000 114/ 0960 000 227<br>E-mail: info@holveryproperty.example</p>
  </div>
</section>
<div class="caption" style="left:484px;top:543px">PAGE-1</div>

<!-- PAGE 2 -->
<section class="page inside-right">
  <div class="band"></div>
  <div class="band-title">SMART MOVE</div>
  <div class="abs" style="left:19px;top:52px;width:308px">
    <div class="h">SERVICES AND <b>BUSINESS LINES</b></div>
    <p class="tiny">Holvery Mgt Consulting serves our clients through four main business lines with services for all property types and asset classes.</p>

    <div class="h" style="margin-top:10px">ADVISORY <b>SERVICES</b></div>
    <p class="tiny">Our advisory services help communities find strategic practical solutions for the most challenging issues facing today's urban, suburban and rural areas.<br>We provide expert, independent, timely, candid and unbiased input from national real estate, land use, design and planning experts. We help communities gain fresh insight and come to innovative solutions for complex land use and real estate development challenges.<br>Our work aims to work with local governments, private developers, community development corporations and many other organizations to address the most challenging real estate and land use issues facing the communities today.<br>Holvery Mgt consulting works with industry leaders including developers, planners, financiers, market analysts, designers, economists, engineers, architects, construction managers, quantity surveyors and public officials to provide practical and objective advise that is not available from any other source.</p>

    <div class="h" style="margin-top:8px">PROPERTY <b>CONSULTANCY</b></div>
    <p class="tiny">As the property market has matured, we have provided consultancy advice to clients in the areas of relocation, market overview, research, planning and development, and property investment.</p>
    <ul class="ticks" style="margin:6px 0 0 46px;width:230px">
      <li class="lead">Our consultancy services include:</li>
      <li>Landlord and Tenant representation</li>
      <li>Acquisition, Leasing and Disposal advice</li>
      <li>Market research/analysis</li>
      <li>Facilities Management advisory</li>
      <li>Planning and development</li>
      <li>Highest and Best Use Studies</li>
      <li>Property management advisory</li>
    </ul>

    <div class="h" style="margin-top:8px">URBAN PLANNING <b>AND DEVELOPMENT</b></div>
    <p class="tiny">Urban planning and development involves the design and organization of urban space and activities.<br>We undertake due diligence and feasibility studies for landowners, developers and investors as regards the processes and considerations involved in development.<br>We also undertake market analysis and demand forecasting; development feasibility and risk assessment; and make recommendations on how to implement an effective development project, including marketing and attracting potential development partners.</p>
    <p class="tiny" style="margin-top:5px"><b style="color:var(--navy)">VALUATION SERVICES</b> – Holvery Mgt provides comprehensive valuation, advisory and consulting services for real estate owners, investors and lenders, combining our specialized expertise and premier technologies to deliver industry-leading valuation reports and analysis.<br>We focus on the valuation of various land and building assets, including agricultural, commercial, industrial, residential, retail, development sites and specialized properties.<br>We act for private and public companies, government and international agencies, banks and insurance companies, trusts and pension funds and individual investors.</p>
    <div style="text-align:center;font-size:5px;font-weight:700;color:var(--navy);margin-top:8px">USES OF VALUATION SERVICES:</div>
    <ul class="ticks" style="margin:8px 0 0 46px;width:240px">
      <li>Auction reserves valuations</li>
      <li>Legal/ Judgment purposes</li>
      <li>Collateral Valuations</li>
      <li>Property Transfer Tax</li>
      <li>Financial Reporting</li>
      <li>Purchase and/or Sale among others</li>
      <li>Insurance Valuations</li>
      <li>Rental Valuations</li>
    </ul>
  </div>
  <div class="abs" style="left:19px;top:458px;font-family:'Michroma',sans-serif;font-size:4.6px;color:var(--navy)">HOLVERY REAL ESTATE</div>
  <div class="abs" style="left:96px;top:461px;width:230px;height:.6px;background:#cfcfcf"></div>
</section>
<div class="caption" style="left:84px;top:1109px">PAGE-2</div>

<!-- BACK -->
<section class="page back">
  <div class="photo" role="img" aria-label="Faint city skyline fading into white" style="left:0;top:300px;width:342px;height:184px;background:linear-gradient(180deg,#fff 0%,#ececec 50%,#e0e0e0 100%)"></div>
  <div class="abs" style="left:0;top:226px;width:342px">
    <div class="brand" style="font-size:10.5px">HOLVERY REAL ESTATE</div>
    <div class="brand-sub">REGISTERED PROPERTY VALUATION SURVEYORS</div>
  </div>
  <div class="abs" style="left:0;top:388px;width:342px;text-align:center;font-size:11px;color:var(--navy)">Contact Us:</div>
  <svg class="abs" style="left:155px;top:404px" width="34" height="9" viewBox="0 0 34 9">
    <path d="M4 0a3 3 0 0 1 3 3c0 2-3 6-3 6S1 5 1 3a3 3 0 0 1 3-3z" fill="#222"/>
    <circle cx="4" cy="3" r="1" fill="#fff"/>
    <path d="M12 1l2 0 1 2-1 1a5 5 0 0 0 2 2l1-1 2 1v2a7 7 0 0 1-7-7z" fill="#222"/>
    <circle cx="28" cy="4.5" r="3.8" fill="none" stroke="#222" stroke-width="1"/>
    <line x1="24.2" y1="4.5" x2="31.8" y2="4.5" stroke="#222" stroke-width=".7"/>
    <ellipse cx="28" cy="4.5" rx="1.6" ry="3.8" fill="none" stroke="#222" stroke-width=".7"/>
  </svg>
  <div class="abs" style="left:0;top:423px;width:342px;text-align:center;font-size:5.6px;line-height:1.5;color:#222">Messrs. Holvery Management Consulting<br>Unit 7 of Plot No. 2218 Meridian Road Kafue, Lusaka</div>
  <div class="abs" style="left:0;top:446px;width:342px;text-align:center;font-size:5.6px;color:#222">+260 900 000 114/ 0960 000 227</div>
  <div class="abs" style="left:0;top:458px;width:342px;text-align:center;font-size:5.6px;color:#222">info@holveryproperty.example</div>
</section>
<div class="caption" style="left:482px;top:1109px">BACK</div>

</body>
</html>
```